Re-Brand of TwigLoom along with a new website design

TwigLoom Ltd are a software & database development company using technologies such as PHP, C#, HTML, JQuery, Flex, AS3, MySQL, Oracle, MSSQL. We like to target all types of business from small to large.

We are great at coding but rubbish at design so thats where we need your help!

We want a complete re-brand of TwigLoom including logo, website design, and business cards.

We would like a design that is clean but other than that, please feel free to be creative.

****Logo****
We are looking for a logo that appears professional but with a splash of colour that indicates a creative side. Please see below some logos that we like the look of:

We like this one because it has a nice simple and clear font for the name of the company but also an icon which is colourful and stands out. http://markvault.example/2013/03/brightnook/

We like this one because it is very clean, simple and again very clear. http://markvault.example/2013/03/tallvoices/

http://markvault.example/2013/03/iron-mule/
http://markvault.example/2013/02/brixwell/
http://markvault.example/2013/01/craft-gallery-norland/

As you will see from all of these examples, the font is very clear but there is always a graphic representing the company too. This is what we like.

****Website****
These are some of the examples of websites we like:
https://www.tillquay.example/
https://www.chatterlane.example/home
http://www.gilbertlensworks.example/
http://www.vestano.example/
http://quillmark.example/
https://www.usedealcrate.example/personal-intros
http://www.newtpanel.example/

The current site can be found at twigloom.co.uk

Requirements
Must have
• Website must have the following pages
Home
Services
Projects
About Us
Contact Us

```html
<!DOCTYPE html>
<html lang="en">
<head>
<meta charset="utf-8">
<title>TwigLoom – Mobile App &amp; Website Development</title>
<link href="https://fonts.googleapis.com/css2?family=PT+Sans:wght@400;700&family=PT+Sans+Narrow:wght@400;700&display=swap" rel="stylesheet">
<style>
:root{
  --header-bg:#2b2b2b;
  --green-light:#9fd20c;
  --green-mid:#74b60a;
  --green-dark:#4a960a;
  --green-deep:#2f4f08;
  --accent:#7ab317;
  --text:#555;
  --heading:#333;
  --card:#f3f3f3;
  --footer:#2c2c2c;
  --footer-bottom:#232323;
  --footer-text:#cfcfcf;
}
*{box-sizing:border-box;margin:0;padding:0}
html,body{width:824px;height:1200px;overflow:hidden;background:#fff}
body{position:relative;font-family:"PT Sans",Arial,sans-serif;color:var(--text)}
.abs{position:absolute}

/* header */
.site-header{left:0;top:0;width:824px;height:76px;background:var(--header-bg)}
.brand{left:52px;top:22px;display:flex;align-items:center;gap:8px}
.brand-dot{width:14px;height:14px;border-radius:50%;background:var(--green-light)}
.brand-name{font-family:"PT Sans Narrow",sans-serif;font-weight:700;font-size:30px;color:#fff;letter-spacing:1px;line-height:1}
.main-nav{right:56px;top:34px;display:flex;font-size:13px}
.main-nav a{color:#fff;text-decoration:none;padding:0 13px;border-left:1px solid #444;line-height:20px}
.main-nav a:first-child{border-left:0}

/* hero */
.hero{left:0;top:76px;width:824px;height:321px;background:linear-gradient(180deg,var(--green-light) 0%,var(--green-mid) 55%,var(--green-dark) 100%)}
.hero-title{left:51px;top:64px;font-family:"PT Sans Narrow",sans-serif;font-weight:700;font-size:29px;line-height:33px;color:#fff}
.hero-title span{color:var(--green-deep)}
.hero-text{left:50px;top:137px;width:260px;font-size:11.5px;line-height:18px;color:#fff}
.hero-dots{left:53px;top:238px;display:flex;gap:4px}
.hero-dots i{width:8px;height:8px;border-radius:50%;background:rgba(255,255,255,.55)}
.hero-devices{left:325px;top:8px;width:455px;height:292px;border-radius:10px;background:linear-gradient(135deg,#3a3a3a 0%,#e8ecef 45%,#cfd8de 70%,#2c2c2c 100%)}

/* intro */
.section-title{font-family:"PT Sans Narrow",sans-serif;font-weight:700;font-size:22px;color:var(--heading);line-height:1}
.welcome-title{left:45px;top:434px}
.welcome-body{left:46px;top:463px;width:460px;font-size:9.6px;line-height:14.5px;text-align:justify}
.welcome-body p{margin-bottom:10px}
.services-title{left:537px;top:434px;color:var(--accent)}
.service-box{left:538px;top:463px;width:240px;height:138px;background:var(--card);box-shadow:0 2px 3px rgba(0,0,0,.15);text-align:center}
.service-icon{position:absolute;left:94px;top:12px;width:52px;height:52px;border-radius:4px;background:linear-gradient(135deg,#cfe3f5,#4d8ed0)}
.service-name{position:absolute;left:0;top:78px;width:100%;font-size:13px;color:#222}
.service-desc{position:absolute;left:30px;top:95px;width:180px;font-size:9.6px;line-height:14px}
.service-arrow{position:absolute;top:55px}
.divider{left:42px;top:636px;width:742px;height:1px;background:#e2e2e2}

/* projects */
.projects-title{left:45px;top:663px}
.project-card{top:693px;width:233px;height:153px;background:var(--card);box-shadow:0 3px 4px rgba(0,0,0,.06)}
.project-media{width:233px;height:104px}
.project-name{position:absolute;left:19px;top:113px;font-size:11.5px;color:#333}
.project-meta{position:absolute;left:19px;top:129px;font-size:11px}

/* partners */
.partners{left:0;top:884px;width:824px;height:62px;background:linear-gradient(180deg,#f2f2f2,#fff 50%,#f2f2f2);display:flex;justify-content:center;align-items:center;gap:32px}
.partner-badge{width:44px;height:20px;border-radius:4px;background:#c9c9c9}
.partner-badge.round{width:30px;height:30px;border-radius:50%}
.accent-bar{left:0;top:946px;width:824px;height:5px;background:var(--accent)}

/* footer */
.site-footer{left:0;top:951px;width:824px;height:201px;background:var(--footer)}
.footer-heading{font-size:14px;color:#fff}
.footer-col{top:32px;color:var(--footer-text);font-size:10.5px}
.contact-col{left:74px}
.contact-col dl{margin-top:12px;line-height:17px}
.contact-col .phone{font-size:15px;color:#fff}
.contact-col .label{font-size:9.5px;color:#bbb}
.blog-col{left:297px;width:205px;font-size:8.5px;line-height:14.5px}
.blog-col p{margin-top:10px}
.blog-col b{color:#fff}
.touch-col{left:566px}
.social-row{display:flex;gap:3px;margin-top:12px}
.social-row i{width:23px;height:23px;border-radius:50%;background:#eee}
.social-links{margin-top:10px;font-size:9px;color:#eee;padding-left:7px}
.footer-rule{top:36px;height:115px;border-left:1px dashed #555}
.footer-bottom{left:0;top:1152px;width:824px;height:48px;background:var(--footer-bottom)}
.copyright{left:57px;top:20px;font-size:8px;color:#aaa}
.bottom-nav{right:50px;top:18px;font-size:9.5px;color:#eee}
.bottom-nav span{color:#888;padding:0 5px}
</style>
</head>
<body>

<header class="site-header abs">
  <div class="brand abs"><span class="brand-dot"></span><span class="brand-name">TWIG LOOM</span></div>
  <nav class="main-nav abs">
    <a href="#">Main</a><a href="#">About Us</a><a href="#">What We Do</a><a href="#">Projects</a><a href="#">Contact Us</a>
  </nav>
</header>

<section class="hero abs">
  <h1 class="hero-title abs">Mobile App &amp; Website<br><span>Development</span></h1>
  <p class="hero-text abs">Class aptent taciti sociosqu ad litora torquent per conubia nostra, per inceptos hymenaeos. Proin nulla arcu, nonummy luctus, dictum eget, fermentum et, lorem</p>
  <div class="hero-dots abs"><i></i><i></i><i></i><i></i></div>
  <div class="hero-devices abs" role="img" aria-label="Tablet, laptop and phone showing client websites and apps"></div>
</section>

<h2 class="section-title welcome-title abs">Welcome to TwigLoom Website Mainpage</h2>
<div class="welcome-body abs">
  <p>if you are looking for web, software, or IT services that really deliver but you don't want to pay over the odds then TwigLoom is the right team for you.</p>
  <p>Based in Harwick our clients are both local, national, both large and small. You may be a start-up business in need of a 'get me up and running quickly' website, or a multi-million pound brand looking for an all singing, all dancing bespoke app. Maybe you are experiencing the pains and pleasures of growing your business and its time to improve your branding and to trade in your current home spun website for something more professional.</p>
  <p>Let's chat today about where we can take your business.</p>
</div>

<h2 class="section-title services-title abs">Services We Provide</h2>
<div class="service-box abs">
  <div class="service-icon" role="img" aria-label="Website development icon"></div>
  <svg class="service-arrow" style="left:17px" width="10" height="20" viewBox="0 0 10 20"><path d="M9 1 1 10l8 9" fill="none" stroke="#aaa" stroke-width="1.5"/></svg>
  <svg class="service-arrow" style="right:17px" width="10" height="20" viewBox="0 0 10 20"><path d="M1 1l8 9-8 9" fill="none" stroke="#aaa" stroke-width="1.5"/></svg>
  <div class="service-name">Website Development</div>
  <div class="service-desc">Proin nulla arcu, nonummy luctus, dictum eget, fermentum et, lorem.</div>
</div>

<div class="divider abs"></div>

<h2 class="section-title projects-title abs">Our Projects</h2>
<article class="project-card abs" style="left:43px">
  <div class="project-media" role="img" aria-label="Phone app resting on a laptop keyboard" style="background:linear-gradient(135deg,#1d1d1d,#8a8f93 60%,#2b2b2b)"></div>
  <div class="project-name">Project tittle here</div><div class="project-meta">Maecenas aliquet velit vel turpis.</div>
</article>
<article class="project-card abs" style="left:297px">
  <div class="project-media" role="img" aria-label="Laptop and tablet showing a shop website" style="background:linear-gradient(135deg,#111,#d8d8d8 55%,#333)"></div>
  <div class="project-name">Project tittle here</div><div class="project-meta">Maecenas aliquet velit vel turpis.</div>
</article>
<article class="project-card abs" style="left:551px">
  <div class="project-media" role="img" aria-label="Colourful advertising website layout" style="background:linear-gradient(120deg,#f4f4f4 10%,#2a7fd0 35%,#f2c21b 65%,#e23b3b 90%)"></div>
  <div class="project-name">Project tittle here</div><div class="project-meta">Maecenas aliquet velit vel turpis.</div>
</article>

<div class="partners abs" aria-label="Accreditations">
  <i class="partner-badge"></i><i class="partner-badge"></i><i class="partner-badge"></i><i class="partner-badge"></i><i class="partner-badge"></i><i class="partner-badge round"></i><i class="partner-badge"></i><i class="partner-badge"></i><i class="partner-badge round"></i>
</div>
<div class="accent-bar abs"></div>

<footer class="site-footer abs">
  <div class="footer-col contact-col abs">
    <h3 class="footer-heading">Contact Information</h3>
    <dl>
      <div><span class="label">Phone: </span><span class="phone">+01632 960 418</span></div>
      <div>&nbsp;Email:&nbsp; contact@twigloom.co.uk</div>
      <div>&nbsp;Add:&nbsp;&nbsp;&nbsp; 42 Fernbrook Lane, Harwick</div>
      <div style="padding-left:33px">Eastshire HW4 7QX</div>
    </dl>
  </div>
  <div class="footer-rule abs" style="left:267px"></div>
  <div class="footer-col blog-col abs">
    <h3 class="footer-heading">Recent Blog</h3>
    <p><b>Mauris vel @</b> lacus vitae felis vestibulum volutpat. Etiam est nunc, venenatis in, tristique</p>
    <p><b>John vel @</b> Sed metus augue, convallis et, vehicula ut, pulvinar eu, ante. Integer orci tellus, tristique vitae, consequat nec, porta vel, lectus.</p>
  </div>
  <div class="footer-rule abs" style="left:526px"></div>
  <div class="footer-col touch-col abs">
    <h3 class="footer-heading">Get In Touch With Us</h3>
    <div class="social-row"><i></i><i></i><i></i><i></i></div>
    <div class="social-links">Circlefeed&nbsp; / &nbsp;Chirpline&nbsp; / &nbsp;Workmesh&nbsp; / &nbsp;RSS</div>
  </div>
</footer>

<div class="footer-bottom abs">
  <div class="copyright abs">Copyright © 2012 Company Name.&nbsp; All right reserved</div>
  <nav class="bottom-nav abs">Main<span>|</span>About Us<span>|</span>What We Do<span>|</span>Our Projects<span>|</span>Contact Us</nav>
</div>

</body>
</html>
```